Morning Lantern Drive Flyer

I need a DL sized flyer that will be sent out to participants in our Morning Lantern Drive - sharing 1million Lantern Cards with the world. This flyer will form the first tangible item most of our community will receive from Brightwater Circle, so it needs to be able to communicate our goal of inspiring change, possibility, kindness and love in the world.

Target Market(s)

Women aged 30 - 50, sophisticated, generous, philanthropy minded, contemporary, elegant

Font styles to use
Sans Serif
Other font styles liked:
• Raleway

Colors

Designer to choose colors to be used in the design.

Requirements
Must have
• Must be DL size - i.e. one third of an A4. On one side the flyer must also include space for the Lantern Cards to be stuck - the lantern cards are Stickmarks that are 3in (76mm) square.
• The logo must be included somewhere, along with the website and social media icons - brightwatercircle.com.au, Facebook, Instagram, Twitter all @brightwatercircle.
• The copy for the flyer is:
• Thank you so much for helping us to reach our goal of having one million lantern cards out in the world. Share one of our notes with a friend, a family member, with a total stranger, or perhaps just with yourself. And remember that you might just be Brightwater Circle in someone else's day.
• Share the story of your lantern cards on social media with the hashtag #morninglanterndrive or send us a photo and your story to lantern@brightwatercircle.com.au

```html
<!DOCTYPE html>
<html lang="en">
<head>
<meta charset="utf-8">
<title>Morning Lantern Drive Flyer</title>
<link rel="stylesheet" href="https://fonts.googleapis.com/css2?family=Oswald:wght@300;400;700&family=PT+Sans+Narrow&family=PT+Sans:ital@1&family=Raleway:wght@500&display=swap">
<style>
  :root {
    --mist: #dcdbe4;
    --navy: #1f1d46;
    --plum: #4c1f5f;
    --magenta: #c0216a;
    --white: #ffffff;
    --ink: #232150;
  }
  * { margin: 0; padding: 0; box-sizing: border-box; }
  html, body { width: 1200px; height: 2542px; overflow: hidden; }
  body { background: var(--navy); font-family: "PT Sans Narrow", sans-serif; }

  .flyer { position: relative; width: 1200px; height: 2542px; overflow: hidden; }

  .brand-band {
    position: absolute; left: 0; top: 0; width: 1200px; height: 576px;
    background: linear-gradient(180deg, #e1e0e8 0%, var(--mist) 100%);
    display: flex; align-items: center; justify-content: center;
  }
  .brand-name {
    font-family: "Raleway", sans-serif; font-weight: 500;
    font-size: 74px; color: var(--ink); letter-spacing: 2px;
    display: flex; align-items: center; gap: 28px;
  }
  .brand-dot { width: 34px; height: 34px; border-radius: 50%; background: var(--magenta); }

  .message-panel {
    position: absolute; left: 0; top: 576px; width: 1200px; height: 1966px;
    background: linear-gradient(160deg, var(--navy) 0%, var(--navy) 45%, var(--plum) 100%);
  }
  .swoosh { position: absolute; left: 0; top: 0; width: 1200px; height: 1966px; }

  .headline {
    position: absolute; left: 0; top: 612px; width: 1200px;
    text-align: center; color: var(--white);
    font-family: "Oswald", sans-serif; font-weight: 300;
    text-shadow: 0 4px 8px rgba(0,0,0,0.45);
    line-height: 1;
  }
  .headline b { font-weight: 700; }
  .headline .line { display: block; font-size: 112px; height: 115px; white-space: nowrap; }
  .headline .line-large { font-size: 112px; height: 140px; line-height: 140px; }
  .headline .line-large b { font-size: 138px; }

  .copy {
    position: absolute; left: 66px; top: 1012px; width: 1068px;
    color: var(--white); font-size: 40px; line-height: 46px; letter-spacing: -0.3px;
  }
  .copy p + p { margin-top: 30px; }
  .copy .row {
    display: block; white-space: nowrap;
    text-align: justify; text-align-last: justify;
  }
  .copy .row-end { text-align: center; text-align-last: center; }

  .contact-bar {
    position: absolute; left: 0; top: 1454px; width: 1200px; height: 114px;
    background: var(--magenta);
    display: flex; align-items: center; justify-content: center;
    font-family: "PT Sans", sans-serif; font-style: italic;
    color: var(--white); font-size: 37px; gap: 24px; white-space: nowrap;
  }
  .social-dot {
    width: 46px; height: 46px; border-radius: 50%;
    border: 3px solid var(--white); flex: none;
  }

  .card-slot {
    position: absolute; left: 137px; top: 1600px; width: 926px; height: 926px;
    background: var(--white);
  }
</style>
</head>
<body>
<div class="flyer">
  <header class="brand-band">
    <div class="brand-name"><span class="brand-dot"></span>Brightwater Circle</div>
  </header>

  <section class="message-panel">
    <svg class="swoosh" viewBox="0 0 1200 1966" role="img" aria-label="Soft violet light streaks across the background">
      <defs>
        <linearGradient id="streak" x1="0" y1="0" x2="1" y2="1">
          <stop offset="0" stop-color="#7a2d7a" stop-opacity="0"/>
          <stop offset="0.5" stop-color="#7a2d7a" stop-opacity="0.35"/>
          <stop offset="1" stop-color="#b02a78" stop-opacity="0.1"/>
        </linearGradient>
      </defs>
      <path d="M120 0 C 420 500, 700 900, 1200 1300 L 1200 1966 C 800 1400, 500 900, 0 300 Z" fill="url(#streak)"/>
    </svg>
  </section>

  <h1 class="headline">
    <span class="line"><b>Goal</b> of <b>Inspiring</b> change</span>
    <span class="line"><b>Possibility, Kindness</b> &amp;</span>
    <span class="line line-large"><b>Love</b> in the <b>World</b></span>
  </h1>

  <div class="copy">
    <p>
      <span class="row">Thank you so much for helping us to reach our goal of having one</span>
      <span class="row">million lantern cards out in the world. Share one of our notes</span>
      <span class="row">with a friend, a family member, with a total stranger, or perhaps just</span>
      <span class="row">with yourself. And remember that you might just be Brightwater</span>
      <span class="row row-end">Circle in someone else's day.</span>
    </p>
    <p>
      <span class="row">Share the story of your lantern cards on social media with the</span>
      <span class="row">hashtag #morninglanterndrive or send us a photo and your story to</span>
      <span class="row row-end">lantern@brightwatercircle.com.au</span>
    </p>
  </div>

  <div class="contact-bar">
    <span>brightwatercircle.com.au,</span>
    <span class="social-dot" aria-label="Social profile"></span>
    <span class="social-dot" aria-label="Social profile"></span>
    <span class="social-dot" aria-label="Social profile"></span>
    <span>all @brightwatercircle.</span>
  </div>

  <div class="card-slot" aria-label="Space for a Lantern Card"></div>
</div>
</body>
</html>
```